Home Remodeler Needs a Website!

Single page (plus contact form) website for small home remodeling company. He's got a few pictures he'd like on the site and needs some basic text. He likes clean, simple designs and is "more traditional" in his stylistic preferences. Most of his business comes from word-of-mouth advertising and so the site is just something he needs for people to feel more comfortable with his business.
Updates

Target Market(s)

People who want to remodel their homes

Coding

Coded - Design and coding required

Number of Pages Required

2 page

Requirements
Must have
• Main page to include some or all of the attached images, contact page. Neutral colors. Old domain: brindlecoveroofing.com New domain: mq-outfitters.com You can pull text from the old site or update it.
Should not have
• No loud colors/loud visual elements

```html
<!DOCTYPE html>
<html lang="en">
<head>
<meta charset="utf-8">
<title>Brindle Cove Homes</title>
<link href="https://fonts.googleapis.com/css2?family=Roboto:wght@400;500;700&family=Lato:wght@400;700&display=swap" rel="stylesheet">
<style>
:root{
  --green:#5c9460;
  --green-dark:#1f3a1d;
  --green-mid:#2e4e2b;
  --ink:#333333;
  --muted:#666666;
  --panel:#f1f1f1;
  --footer:#222222;
  --footer-bar:#161616;
  --card:#5a5a5a;
  --white:#ffffff;
}
*{box-sizing:border-box;margin:0;padding:0}
html,body{width:1200px;height:4222px;overflow:hidden}
body{position:relative;font-family:'Lato',sans-serif;color:var(--ink);background:var(--white)}
.abs{position:absolute}
.photo{position:absolute}
/* header */
.hero{position:absolute;left:0;top:0;width:1200px;height:713px;background:linear-gradient(135deg,#5a4a3a 0%,#7a6450 35%,#4e4034 65%,#2e261f 100%)}
.hero-shade{position:absolute;inset:0;background:linear-gradient(90deg,rgba(0,0,0,.35),rgba(0,0,0,.05) 60%,rgba(0,0,0,.2))}
.topbar{position:absolute;left:0;top:0;width:1200px;height:54px;background:rgba(0,0,0,.55);border-bottom:1px solid rgba(255,255,255,.15)}
.brand{position:absolute;left:148px;top:12px;font-family:'Roboto',sans-serif;font-weight:700;font-size:25px;color:var(--white)}
.phone{position:absolute;left:820px;top:17px;font-family:'Roboto',sans-serif;font-size:14px;color:var(--white);display:flex;gap:8px;align-items:center}
.mail-ic{position:absolute;left:975px;top:19px}
.estimate{position:absolute;left:1036px;top:0;width:164px;height:54px;background:var(--green);color:var(--white);font-family:'Roboto',sans-serif;font-size:13px;font-weight:500;line-height:15px;padding:11px 0 0 55px}
.estimate svg{position:absolute;left:7px;top:15px}
.nav{position:absolute;top:70px;left:0;width:1200px;display:flex;justify-content:center;font-family:'Roboto',sans-serif;font-weight:500;font-size:13px;color:var(--white)}
.nav span{padding:0 30px;border-right:1px solid rgba(255,255,255,.35);line-height:15px}
.nav span:last-child{border-right:none}
.hero-kicker{position:absolute;left:226px;top:222px;color:var(--white);font-size:17px;font-family:'Roboto',sans-serif}
.hero-title{position:absolute;left:226px;top:255px;color:var(--white);font-family:'Roboto',sans-serif;font-weight:700;font-size:44px;line-height:52px}
.hero-text{position:absolute;left:226px;top:372px;width:440px;color:var(--white);font-size:18px;line-height:26px;font-family:'Roboto',sans-serif}
.btn{display:inline-block;background:var(--green);color:var(--white);font-family:'Roboto',sans-serif;font-weight:500;text-align:center}
.hero-btn{position:absolute;left:226px;top:451px;width:160px;height:42px;line-height:42px;border-radius:21px;font-size:15px}
.arrow{position:absolute;top:314px;width:40px;height:40px;border:2px solid var(--white);border-radius:50%}
.dots{position:absolute;left:578px;top:573px;display:flex;gap:10px}
.dots i{display:block;width:13px;height:13px;border:2px solid var(--white);border-radius:50%}
.dots i.on{background:var(--white)}
/* welcome */
.welcome-kicker{position:absolute;left:687px;top:823px;font-size:13px;font-weight:700;font-family:'Roboto',sans-serif;color:#222}
.welcome-title{position:absolute;left:687px;top:853px;font-family:'Roboto',sans-serif;font-weight:500;font-size:28px;line-height:34px;color:#222}
.welcome-text{position:absolute;left:687px;top:938px;width:360px;font-size:13px;line-height:22.5px;color:var(--muted)}
.small-btn{position:absolute;left:687px;top:1100px;width:108px;height:34px;line-height:34px;font-size:13px;border-radius:2px}
/* contracting */
.contracting{position:absolute;left:0;top:1237px;width:1200px;height:648px;background:linear-gradient(180deg,var(--green-dark),var(--green-mid) 50%,#213d1f)}
.sec-title-white{position:absolute;top:1295px;width:1200px;text-align:center;color:var(--white);font-family:'Roboto',sans-serif;font-weight:500;font-size:30px}
.rule{position:absolute;left:575px;top:1342px;width:50px;height:3px;background:var(--green)}
.svc{position:absolute;width:297px;height:200px;text-align:center;color:var(--white)}
.svc.hl{background:rgba(92,148,96,.45)}
.svc .ic{margin-top:28px;height:52px}
.svc h3{font-family:'Lato',sans-serif;font-weight:400;font-size:18px;margin-top:9px}
.svc p{font-size:11.5px;line-height:18px;width:240px;margin:6px auto 0;color:#dfe7de}
.svc .btn{width:100px;height:26px;line-height:26px;border-radius:13px;font-size:11px;margin-top:12px;font-weight:400}
.vline{position:absolute;width:1px;background:rgba(255,255,255,.12)}
/* services */
.kicker-c{position:absolute;width:1200px;text-align:center;font-family:'Roboto',sans-serif;font-size:13px;color:#333}
.sec-title{position:absolute;width:1200px;text-align:center;font-family:'Roboto',sans-serif;font-weight:500;font-size:33px;color:#333}
.sec-title em{font-style:normal;color:var(--green)}
.offer{position:absolute;width:200px;font-family:'Roboto',sans-serif}
.offer h4{font-size:12px;font-weight:700;color:#222}
.offer p{font-size:11px;line-height:17px;color:#444;margin-top:4px}
.offer.l{text-align:right}
/* projects */
.proj{position:absolute}
/* testimonials */
.quote{position:absolute;width:277px;height:129px;background:var(--card);color:var(--white);padding:18px 20px}
.quote h5{font-size:13px;font-weight:700}
.quote p{font-size:10.5px;line-height:17px;margin-top:6px;color:#eee;font-family:'Roboto',sans-serif}
.quote::after{content:"";position:absolute;left:18px;bottom:-16px;border-left:0 solid transparent;border-right:16px solid transparent;border-top:16px solid var(--card)}
.person{position:absolute;display:flex;gap:10px;align-items:center}
.avatar{width:44px;height:44px;background:linear-gradient(135deg,#c9b29a,#8a7262)}
.person b{display:block;font-size:13.5px;color:#333;font-weight:400}
.person small{font-size:11px;color:#888}
/* contact */
.touch{position:absolute;left:0;top:3426px;width:1200px;height:455px;background:var(--panel)}
.field{position:absolute;background:var(--white);border:1px solid #e2e2e2;box-shadow:0 1px 3px rgba(0,0,0,.05);font-family:'Roboto',sans-serif;font-size:14px;color:#888;padding:0 20px}
.submit{position:absolute;left:528px;top:3791px;width:142px;height:43px;line-height:43px;font-size:13px;font-weight:700;border-radius:2px}
/* footer */
.footer{position:absolute;left:0;top:3881px;width:1200px;height:290px;background:var(--footer);color:#ccc}
.f-head{position:absolute;font-family:'Roboto',sans-serif;font-weight:500;font-size:13px;color:var(--white)}
.f-item{position:absolute;font-size:12px;color:#bbb;font-family:'Roboto',sans-serif}
.f-item small{display:block;font-size:11px;color:#999;margin-top:4px}
.f-ic{position:absolute;width:36px;height:36px;border-radius:50%;background:#2e2e2e}
.f-link{position:absolute;left:541px;font-size:11.5px;color:#bbb;font-family:'Roboto',sans-serif}
.f-link::before{content:"›";color:var(--green);margin-right:9px;font-size:14px}
.sub{position:absolute;left:739px;top:3973px;width:308px;height:36px;border-radius:18px;background:var(--white);overflow:hidden;font-size:13px;font-family:'Roboto',sans-serif}
.sub span{position:absolute;left:22px;top:10px;color:#888}
.sub b{position:absolute;right:0;top:0;width:104px;height:36px;line-height:36px;text-align:center;background:var(--green);color:var(--white);font-weight:400;font-size:14px}
.social{position:absolute;top:4080px;width:36px;height:36px;border-radius:50%;background:var(--green)}
.copy{position:absolute;left:0;top:4171px;width:1200px;height:51px;background:var(--footer-bar);color:#999;font-size:11px;text-align:center;line-height:51px;font-family:'Roboto',sans-serif}
</style>
</head>
<body>

<!-- HERO -->
<section class="hero" role="img" aria-label="Photo of a remodeled basement room with polished concrete floor, wood plank wall and french doors">
  <div class="hero-shade"></div>
</section>
<header>
  <div class="topbar"></div>
  <div class="brand">Brindle Cove Homes</div>
  <div class="phone">
    <svg width="16" height="16" viewBox="0 0 24 24" fill="none" stroke="#fff" stroke-width="2"><path d="M22 16.9v3a2 2 0 0 1-2.2 2 19.8 19.8 0 0 1-8.6-3.1 19.5 19.5 0 0 1-6-6A19.8 19.8 0 0 1 2.1 4.2 2 2 0 0 1 4.1 2h3a2 2 0 0 1 2 1.7c.1 1 .4 1.9.7 2.8a2 2 0 0 1-.5 2.1L8 9.9a16 16 0 0 0 6 6l1.3-1.3a2 2 0 0 1 2.1-.4c.9.3 1.8.6 2.8.7a2 2 0 0 1 1.7 2z"/></svg>
    555-014-2270
  </div>
  <svg class="mail-ic" width="22" height="16" viewBox="0 0 22 16" fill="none" stroke="#fff" stroke-width="1.5"><rect x="1" y="1" width="20" height="14"/><path d="M1 1l10 8 10-8M1 15l7-7M21 15l-7-7"/></svg>
  <div class="estimate">
    <svg width="20" height="20" viewBox="0 0 20 20" fill="none" stroke="#fff" stroke-width="1.4"><circle cx="10" cy="10" r="8.5"/><path d="M8.5 6l4 4-4 4"/></svg>
    REQUEST AN<br>ESTIMATE
  </div>
  <nav class="nav"><span>HOME</span><span>ABOUT</span><span>SERVICES ▾</span><span>GALLERY</span><span>CONTACT</span></nav>
</header>
<div class="hero-kicker">Brindle Cove Homes</div>
<h1 class="hero-title">Home Construction &amp;<br>Remodeling</h1>
<p class="hero-text">When you want affordable, quality home construction services think of us to do the job.</p>
<div class="btn hero-btn">LEARN MORE</div>
<div class="arrow" style="left:126px"><svg width="36" height="36" viewBox="0 0 36 36" fill="none" stroke="#fff" stroke-width="2"><path d="M20 12l-6 6 6 6"/></svg></div>
<div class="arrow" style="left:1032px"><svg width="36" height="36" viewBox="0 0 36 36" fill="none" stroke="#fff" stroke-width="2"><path d="M16 12l6 6-6 6"/></svg></div>
<div class="dots"><i></i><i class="on"></i><i></i><i></i></div>
<svg class="abs" style="left:0;top:540px" width="1200" height="180" viewBox="0 540 1200 180">
  <path d="M0 620 Q 560 780 1200 560 L1200 720 L0 720 Z" fill="#fff"/>
  <path d="M0 620 Q 560 780 1200 560" fill="none" stroke="#5c9460" stroke-width="7"/>
</svg>

<!-- WELCOME -->
<div class="photo" style="left:149px;top:802px;width:256px;height:168px;background:linear-gradient(135deg,#2c4f8a,#8b6a45 55%,#d8d2c4)" role="img" aria-label="Kitchen with stainless refrigerator and blue walls"></div>
<div class="photo" style="left:257px;top:987px;width:148px;height:170px;background:linear-gradient(160deg,#4a3526,#7b5335 50%,#1e1814)" role="img" aria-label="Kitchen with dark wood cabinets and bar stools"></div>
<div class="photo" style="left:425px;top:821px;width:198px;height:318px;background:linear-gradient(180deg,#c9d6d9,#9fb0b5 45%,#8a7a66 80%,#6d5e4d)" role="img" aria-label="Remodeled bathroom with soaking tub and window"></div>
<div class="welcome-kicker">WELCOME TO BRINDLE COVE HOMES.</div>
<h2 class="welcome-title">Quality Home Construction<br>Services</h2>
<p class="welcome-text">Since 1981 Martin Quill has built and remodeled over 400 homes and businesses. Let us be your contractor for the next project you start. When quality, value and personal attention to detail are important With over 20 years experience in residential and commercial construction, you can trust your project to Brindle Cove Homes.</p>
<div class="btn small-btn">Learn More</div>

<!-- CONTRACTING -->
<section class="contracting"></section>
<h2 class="sec-title-white">Commercial &amp; Residential Contracting</h2>
<div class="rule"></div>
<div class="vline" style="left:451px;top:1610px;height:190px"></div>
<div class="vline" style="left:751px;top:1610px;height:190px"></div>
<div class="vline" style="left:751px;top:1400px;height:190px"></div>

<div class="svc" style="left:154px;top:1395px">
  <svg class="ic" width="54" height="52" viewBox="0 0 54 52" fill="none" stroke="#fff" stroke-width="1.6"><path d="M4 22L27 5l23 17"/><rect x="9" y="22" width="36" height="26"/><rect x="15" y="28" width="8" height="8"/><rect x="31" y="28" width="8" height="8"/><rect x="23" y="38" width="8" height="10"/></svg>
  <h3>Pre Construction Consultation</h3>
  <p>Duis tincidunt egestas feugiat. In or semper nisi vel imperdiet. Sed venenatis eu.</p>
  <div class="btn">Read More</div>
</div>
<div class="svc hl" style="left:447px;top:1395px">
  <svg class="ic" width="54" height="52" viewBox="0 0 54 52" fill="none" stroke="#fff" stroke-width="1.6"><rect x="10" y="14" width="28" height="30" transform="rotate(-35 24 29)"/><path d="M30 8l14 14M20 30l8 8M38 6l8 8"/></svg>
  <h3>New Construction</h3>
  <p>Duis tincidunt egestas feugiat. In or semper nisi vel imperdiet. Sed venenatis eu.</p>
  <div class="btn">Read More</div>
</div>
<div class="svc" style="left:747px;top:1395px">
  <svg class="ic" width="54" height="52" viewBox="0 0 54 52" fill="none" stroke="#fff" stroke-width="1.6"><rect x="8" y="26" width="38" height="22"/><rect x="13" y="31" width="10" height="8"/><rect x="29" y="31" width="12" height="17"/><path d="M14 26V8h6v18M32 26V12h8v14"/></svg>
  <h3>Remodeling / kitchens and baths</h3>
  <p>Duis tincidunt egestas feugiat. In or semper nisi vel imperdiet. Sed venenatis eu.</p>
  <div class="btn">Read More</div>
</div>
<div class="svc" style="left:154px;top:1612px">
  <svg class="ic" width="54" height="52" viewBox="0 0 54 52" fill="none" stroke="#fff" stroke-width="1.6"><rect x="8" y="30" width="38" height="12"/><path d="M8 42v6M46 42v6M12 30v-8h30v8"/><rect x="26" y="6" width="16" height="12"/></svg>
  <h3>Additions</h3>
  <p>Duis tincidunt egestas feugiat. In or semper nisi vel imperdiet. Sed venenatis eu.</p>
  <div class="btn">Read More</div>
</div>
<div class="svc" style="left:451px;top:1612px">
  <svg class="ic" width="54" height="52" viewBox="0 0 54 52" fill="none" stroke="#fff" stroke-width="1.6"><path d="M8 28L24 14l16 14M13 24v22h22V24"/><circle cx="42" cy="12" r="5"/><path d="M24 46V34"/></svg>
  <h3>Porches &amp; Decks</h3>
  <p>Duis tincidunt egestas feugiat. In or semper nisi vel imperdiet. Sed venenatis eu.</p>
  <div class="btn">Read More</div>
</div>
<div class="svc" style="left:751px;top:1612px">
  <svg class="ic" width="54" height="52" viewBox="0 0 54 52" fill="none" stroke="#fff" stroke-width="1.6"><path d="M8 28L24 14l16 14M13 24v22h22V24"/><circle cx="42" cy="12" r="5"/><path d="M24 46V34"/></svg>
  <h3>Historic Renovations</h3>
  <p>Duis tincidunt egestas feugiat. In or semper nisi vel imperdiet. Sed venenatis eu.</p>
  <div class="btn">Read More</div>
</div>

<!-- SERVICES -->
<div class="kicker-c" style="top:1952px">What We Offer</div>
<h2 class="sec-title" style="top:1974px">Our <em>Services</em></h2>

<svg class="abs" style="left:420px;top:2038px" width="360" height="360" viewBox="0 0 360 360">
  <circle cx="180" cy="180" r="170" fill="none" stroke="#5c9460" stroke-width="2.5"/>
  <g fill="#fff" stroke="#5c9460" stroke-width="2">
    <circle cx="52" cy="69" r="9"/><circle cx="10" cy="180" r="9"/><circle cx="52" cy="291" r="9"/>
    <circle cx="308" cy="69" r="9"/><circle cx="350" cy="180" r="9"/><circle cx="308" cy="291" r="9"/>
  </g>
</svg>
<div class="photo" style="left:457px;top:2075px;width:286px;height:286px;border-radius:50%;background:radial-gradient(circle at 40% 40%,#b89a80,#6d7c8c 60%,#c9a63a)" role="img" aria-label="Family relaxing together on a sofa at home"></div>

<div class="offer l" style="left:143px;top:2072px"><h4>ROOFING</h4><p>Lorem Ipsum is simply<br>dummy text of the printing</p></div>
<svg class="abs" style="left:360px;top:2076px" width="76" height="42" viewBox="0 0 76 42" fill="none" stroke="#5c9460" stroke-width="2"><path d="M2 40L22 2h32l20 38zM12 40L30 6M22 40L40 6M32 40L48 6"/></svg>
<div class="offer l" style="left:113px;top:2190px"><h4>WINDOW REPLACEMENT</h4><p>Lorem Ipsum is simply dummy<br>text of the printing</p></div>
<svg class="abs" style="left:336px;top:2186px" width="52" height="56" viewBox="0 0 52 56" fill="none" stroke="#5c9460" stroke-width="2"><rect x="2" y="2" width="48" height="52"/><path d="M26 2v52M2 28h48"/><rect x="7" y="7" width="14" height="16"/><rect x="31" y="33" width="14" height="16"/></svg>
<div class="offer l" style="left:143px;top:2318px"><h4>ELECTRICAL</h4><p>Lorem Ipsum is simply<br>dummy text of the printing</p></div>
<svg class="abs" style="left:362px;top:2310px" width="52" height="60" viewBox="0 0 52 60" fill="none" stroke="#5c9460" stroke-width="2"><circle cx="26" cy="26" r="12"/><path d="M20 38v10h12V38M22 52h8M26 6V2M8 26H4M48 26h-4M12 12l-3-3M40 12l3-3"/></svg>

<div class="offer" style="left:856px;top:2077px"><h4>AIR CONDITIONING<br>AND PLUMBING</h4><p>Lorem Ipsum is simply<br>dummy text of the printing</p></div>
<svg class="abs" style="left:778px;top:2076px" width="62" height="62" viewBox="0 0 62 62" fill="none" stroke="#5c9460" stroke-width="2"><circle cx="31" cy="14" r="10"/><path d="M31 14l4-4M31 24v12M4 36h54v16H4zM14 36v16M48 36v16"/></svg>
<div class="offer" style="left:883px;top:2188px"><h4>PAINTING</h4><p>Lorem Ipsum is simply dummy<br>text of the printing</p></div>
<svg class="abs" style="left:802px;top:2180px" width="60" height="60" viewBox="0 0 60 60" fill="none" stroke="#5c9460" stroke-width="2"><rect x="30" y="4" width="16" height="28" transform="rotate(40 38 18)"/><path d="M28 30L8 52l4 4 20-22M44 8l12 12"/></svg>
<div class="offer" style="left:852px;top:2311px"><h4>CONCRETE WORK</h4><p>Lorem Ipsum is simply<br>dummy text of the printing</p></div>
<svg class="abs" style="left:778px;top:2305px" width="62" height="64" viewBox="0 0 62 64" fill="none" stroke="#5c9460" stroke-width="2"><rect x="6" y="4" width="50" height="10"/><path d="M31 14v36M24 50h14M20 60h22M12 14v10M50 14v10"/></svg>

<!-- PROJECTS -->
<h2 class="sec-title" style="top:2496px">Latest <em>Projects</em></h2>
<div class="photo" style="left:161px;top:2575px;width:434px;height:434px;background:linear-gradient(170deg,#8f9aa0,#6b5a48 45%,#3d3128 80%,#54463a)" role="img" aria-label="Remodeled basement with concrete floor and french doors"></div>
<div class="photo" style="left:603px;top:2575px;width:435px;height:213px;background:linear-gradient(160deg,#a8b7bc,#c8c4b8 50%,#7a6a58)" role="img" aria-label="Bathroom with soaking tub and tile backsplash"></div>
<div class="photo" style="left:603px;top:2796px;width:213px;height:213px;background:linear-gradient(165deg,#4b3727,#7b5335 50%,#1e1814)" role="img" aria-label="Kitchen with wood cabinets and bar stools"></div>
<div class="photo" style="left:824px;top:2796px;width:214px;height:213px;background:linear-gradient(135deg,#2c4f8a,#8b6a45 55%,#d8d2c4)" role="img" aria-label="Kitchen with refrigerator and farmhouse sink"></div>

<!-- TESTIMONIALS -->
<h2 class="sec-title" style="top:3075px;font-size:29px">Our <em>Client Say</em></h2>
<div class="quote" style="left:161px;top:3148px"><h5>"Quality Design"</h5><p>Donec fringilla nunc vitae facilisis ornar a lacinia non nibh. Maecenas sit amet arcu eget leo pellentesque euismod.</p></div>
<div class="quote" style="left:461px;top:3148px"><h5>"Super Support"</h5><p>Cras id maximus neque, ullamcorper se orn amet, lacinia non nibh. Maecenas sit amet arcu eget leo pellentesque the compen.</p></div>
<div class="quote" style="left:761px;top:3148px"><h5>"Quality Design"</h5><p>Orci varius natoque ullamcorper sed or amet, lacinia non nibh. Maecenas sit amet arcu eget leo pellentesque the euismod.</p></div>
<div class="person" style="left:161px;top:3303px"><div class="avatar" role="img" aria-label="Client portrait"></div><div><b>Dorian Pike</b><small>Designer in Northfield</small></div></div>
<div class="person" style="left:461px;top:3303px"><div class="avatar" role="img" aria-label="Client portrait"></div><div><b>Maren Sollis</b><small>Marketing in Northfield</small></div></div>
<div class="person" style="left:761px;top:3303px"><div class="avatar" role="img" aria-label="Client portrait"></div><div><b>Tobias Wrenn</b><small>Developers in Northfield</small></div></div>

<!-- CONTACT -->
<section class="touch"></section>
<h2 class="sec-title" style="top:3494px;font-size:28px;font-weight:700;color:#222">Get In Touch</h2>
<div class="field" style="left:310px;top:3557px;width:277px;height:42px;line-height:42px">Full name</div>
<div class="field" style="left:611px;top:3557px;width:279px;height:42px;line-height:42px">Email</div>
<div class="field" style="left:311px;top:3627px;width:578px;height:126px;padding-top:16px">Message</div>
<div class="btn submit">SUBMIT</div>

<!-- FOOTER -->
<footer class="footer"></footer>
<div class="f-head" style="left:220px;top:3932px">CONTACT US</div>
<div class="f-ic" style="left:222px;top:3980px"><svg width="36" height="36" viewBox="0 0 36 36" fill="none" stroke="#5c9460" stroke-width="1.6"><rect x="14" y="11" width="8" height="14" rx="1"/></svg></div>
<div class="f-item" style="left:268px;top:3986px">555-014-3381, 555-014-2270<small>Support 24/7 Weekdays</small></div>
<div class="f-ic" style="left:222px;top:4034px"><svg width="36" height="36" viewBox="0 0 36 36" fill="#5c9460"><path d="M18 10a6 6 0 0 0-6 6c0 5 6 11 6 11s6-6 6-11a6 6 0 0 0-6-6zm0 8.5a2.5 2.5 0 1 1 0-5 2.5 2.5 0 0 1 0 5z"/></svg></div>
<div class="f-item" style="left:268px;top:4046px;font-size:11px">Larkspur Court, Fairvale, TN 37000, USA</div>
<div class="f-ic" style="left:222px;top:4086px"><svg width="36" height="36" viewBox="0 0 36 36" fill="none" stroke="#5c9460" stroke-width="1.5"><rect x="11" y="13" width="14" height="10"/><path d="M11 13l7 5 7-5"/></svg></div>
<div class="f-item" style="left:268px;top:4097px;font-size:11px">info@example.com</div>

<div class="f-head" style="left:541px;top:3932px">OUR SERVICES</div>
<div class="f-link" style="top:3970px">Electrical</div>
<div class="f-link" style="top:3998px">Plumbing</div>
<div class="f-link" style="top:4026px">Engine Repair</div>
<div class="f-link" style="top:4053px">Repair House</div>
<div class="f-link" style="top:4081px">Home Maintenance</div>
<div class="f-link" style="top:4109px">Wall Paint</div>

<div class="f-head" style="left:746px;top:3932px">SUBSCRIBE</div>
<div class="sub"><span>Email address</span><b>Subscribe</b></div>
<div class="f-head" style="left:746px;top:4043px">FOLLOW US</div>
<div class="social" style="left:746px" aria-label="Social profile"></div>
<div class="social" style="left:791px" aria-label="Social profile"></div>
<div class="social" style="left:834px" aria-label="Social profile"></div>
<div class="social" style="left:880px" aria-label="Social profile"></div>

<div class="copy">Copyright © 2021 Brindle Cove Homes.</div>
</body>
</html>
```